VerintaCore PowerPoint Presentation Design

I am looking for a PowerPoint design for a new company based in Dallas, Texas called VerintaCore. We provide extremely powerful predictive and prescriptive analytics software focused on the Internet of Things (IoT) market. Our initial products are called VRC Foundry and VRC Pulse. We would like to see designs that support our logo design, which is attached.

I AM LOOKING FOR A THEME TO BE DEVELOPED FOR THE TITLE SLIDE AND INSIDE SLIDES OF A PRESENTATION. I AM NOT LOOKING FOR SOMEONE TO TAKE MY CONTENT AND CREATE A COMPLETE PRESENTATION.

Target Market(s)

Advanced Analytics, Internet of Things

Industry/Entity Type

It Company

Requirements
Must have
• Bolder colors, but they must work with the logo
Nice to have
• I prefer that the design incorporate the them of "connectivity" or "connectedness" to reflect the IoT market and "intelligence" or "smart" to reflect the analytics aspect of the business
Should not have
• I don't want people represented in the graphics scheme

```html
<!DOCTYPE html>
<html lang="en">
<head>
<meta charset="utf-8">
<title>VerintaCore – Content Slide</title>
<link rel="stylesheet" href="https://fonts.googleapis.com/css2?family=Arimo:wght@400;700&display=swap">
<style>
  :root {
    --ink: #000000;
    --muted: #555555;
    --brand-blue: #1f5fd6;
    --rule-blue: #2a63d8;
    --accent-orange: #f7a21b;
    --accent-orange-dark: #f08a00;
    --panel-tint: #f2f2f2;
    --divider: #9a9a9a;
    --footer-ink: #444444;
  }
  * { margin: 0; padding: 0; box-sizing: border-box; }
  html, body { width: 1200px; height: 831px; overflow: hidden; background: #ffffff; }
  body { font-family: "Arimo", Arial, sans-serif; color: var(--ink); position: relative; }

  .slide-title { position: absolute; left: 23px; top: 12px; font-size: 34px; font-weight: 700; letter-spacing: -0.3px; }
  .slide-subtitle { position: absolute; left: 23px; top: 58px; font-size: 28px; color: var(--muted); }

  .brand { position: absolute; right: 28px; top: 30px; display: flex; align-items: center; gap: 8px; }
  .brand-mark { width: 14px; height: 14px; background: var(--accent-orange); }
  .brand-name { font-size: 27px; font-weight: 700; color: var(--brand-blue); letter-spacing: -0.5px; }

  .header-rule { position: absolute; left: 0; top: 108px; width: 1200px; height: 4px;
    background: linear-gradient(90deg, var(--rule-blue) 0%, #7fa3ea 35%, #d9e3f7 70%, rgba(255,255,255,0) 100%); }

  .column { position: absolute; top: 133px; width: 562px; }
  .column-left { left: 23px; }
  .column-right { left: 612px; }

  .heading-one { font-size: 18px; font-weight: 700; padding: 2px 0 5px; border-bottom: 1px solid var(--divider); }
  .heading-two { font-size: 18px; font-weight: 700; height: 35px; line-height: 35px; padding-left: 12px;
    background: linear-gradient(180deg, #fbb93a 0%, var(--accent-orange) 55%, var(--accent-orange-dark) 100%);
    box-shadow: 0 2px 3px rgba(0,0,0,0.25); }

  .panel { background: var(--panel-tint); padding: 10px 12px 12px; min-height: 277px; }
  .column-left .body { padding-top: 9px; }

  .body p, .body li { line-height: 1.25; }
  .level-0 { font-size: 13px; margin-bottom: 3px; }
  .body ul { list-style: none; }
  .body li { position: relative; }
  .level-1 { font-size: 13px; padding-left: 28px; margin-bottom: 6px; }
  .level-1::before { content: ""; position: absolute; left: 5px; top: 5px; width: 7px; height: 7px; background: var(--accent-orange); }
  .level-2 { font-size: 11.5px; padding-left: 56px; margin-bottom: 6px; }
  .level-2::before { content: ""; position: absolute; left: 38px; top: 7px; width: 6px; height: 1px; background: var(--accent-orange); }
  .level-3 { font-size: 10.5px; padding-left: 84px; margin-bottom: 5px; }
  .level-3::before { content: ""; position: absolute; left: 66px; top: 6px; width: 5px; height: 1px; background: var(--accent-orange); }
  .level-4 { font-size: 8.5px; padding-left: 112px; }
  .level-4::before { content: ""; position: absolute; left: 94px; top: 5px; width: 4px; height: 1px; background: var(--divider); }

  .page-number { position: absolute; left: 596px; top: 798px; font-size: 13px; color: var(--footer-ink); }
  .classification { position: absolute; right: 28px; top: 798px; font-size: 13px; color: var(--footer-ink); }
</style>
</head>
<body>
  <h1 class="slide-title">Slide title</h1>
  <p class="slide-subtitle">Subtitle</p>

  <div class="brand">
    <span class="brand-mark"></span>
    <span class="brand-name">VerintaCore</span>
  </div>

  <div class="header-rule"></div>

  <section class="column column-left">
    <h2 class="heading-one">Heading style 1</h2>
    <div class="body">
      <p class="level-0">Body text Body text Body text Body text Body text Body text Body text Body text Body text Body text Body text Body text Body text Body text</p>
      <ul>
        <li class="level-1">Body text Body text Body text Body text Body text Body text Body text Body text Body text Body text Body text Body text Body text Body text Body text</li>
        <li class="level-2">Body text Body text Body text Body text Body text Body text Body text Body text Body text Body text Body text Body text Body text Body text Body text Body text</li>
        <li class="level-3">Body text Body text Body text Body text Body text Body text Body text Body text Body text Body text Body text Body text Body text Body text Body text Body text</li>
        <li class="level-4">Body text Body text Body text Body text Body text Body text Body text Body text Body text Body text Body text Body text Body text Body text Body text Body text Body text</li>
      </ul>
    </div>
  </section>

  <section class="column column-right">
    <h2 class="heading-two">Heading style 2</h2>
    <div class="body panel">
      <p class="level-0">Body text Body text Body text Body text Body text Body text Body text Body text Body text Body text Body text Body text Body text Body text Body text Body text</p>
      <ul>
        <li class="level-1">Body text Body text Body text Body text Body text Body text Body text Body text Body text Body text Body text Body text Body text Body text Body text</li>
        <li class="level-2">Body text Body text Body text Body text Body text Body text Body text Body text Body text Body text Body text Body text Body text Body text Body text</li>
        <li class="level-3">Body text Body text Body text Body text Body text Body text Body text Body text Body text Body text Body text Body text Body text Body text Body text Body text</li>
        <li class="level-4">Body text Body text Body text Body text Body text Body text Body text Body text Body text Body text Body text Body text Body text Body text Body text Body text</li>
      </ul>
    </div>
  </section>

  <span class="page-number">2</span>
  <span class="classification">INTERNAL</span>
</body>
</html>
```